Realtor / Kitchen & Bath Designer / Curb Appeal Specialist Before & After Postcard

Realtor / Curb Appeal Specialist / Kitchen & Bath Designer / Interior Decorator / Real Estate Staging

I need an oversized postcard to send to luxury / waterfront homes and condominiums. I have a background photo and 3 sets of Before and After photos and a professional photo for my bio which I would like to be on the back with room for address labels and postage.

I offer a FREE (No obligation) in-home design / staging consultation for potential homeowners interesed in selling their home or condominium. I will place some of these cards in open houses, related businesses, some will be direct mailed, some will be handed out.

My goal with this marketing is to attract potential SELLERS who realize that they need my skills, ideas, experience for: Curb Appeal / Facade Enhancement / landscaping ... Kitchen & Bath Updating ... Decorating / Paint Colors ... Staging, etc ... in order to help SELL their properties FASTER and with HIGHER NET PROCEEDS on the real estate market ... and HOPEFULLY LISTING their property with me as their Listing Realtor.

I realize this is a bit complicated but I hopfully the photos will mostly convey the message ... with text as needed, more elegantly than I have worded this. Here are some POINTS that I am trying to make:

Curb Appeal, Landscaping, Updated Kitchens & Baths, Paint Colors, Lighting ... are more important than ever ... to sell upscale waterfront homes/condominiums in this competitive market ... design savvy BUYERS are looking for quality fixtures, features, and WOW factors.

Bio. Brennic Dwale is a Florida Realtor and licensed Interior Decorator, Kitchen & Bath Designer, and Curb Appeal Specialist with 25+ years experience in the residential design/remodeling industry.

Photos are: Professional photo (can be cropped and/or B/W with Bio on back) ... Photos are in order: 6 sets of Before - After, with addtional photo.

Target Market(s)

Home and Condo owners who are wanting to SELL their home and hopefully LIST with me as a REALTOR. I also pick up some design work.

Industry/Entity Type

Landscaping

Requirements
Must have
• Front: The entire front could be a faded - muted (half tone) photo of the kitchen (last photo) ... then 3 or 4 sets of smaller before & after pics with borders. The after photos could be slightly larger than the before pics which could be inset or superimposed/offset at the bottom. There should be a lead line at the top such as :

"Serious about selling your home or condominium?" and maybe at the bottom: "Today's design savvy BUYERS desire updated kitchens and baths, quality fixtures, design features, and attractive landscaping."

Back: My bio with photo. Room for hand written or address labels/postage. Perhaps the Before & After of the condo bathroom could also be on the back at the left /top with my photo/bio smaller at the left bottom.
Nice to have
• somehow make it seem classy and elegant ... not like a sales pitch
Should not have
• anything that looks or sounds tacky.

```html
<!DOCTYPE html>
<html lang="en">
<head>
<meta charset="utf-8">
<title>Brennic Dwale – Postcard Back</title>
<link rel="stylesheet" href="https://fonts.googleapis.com/css2?family=Montserrat:ital,wght@0,400;0,500;1,800&display=swap">
<style>
  :root {
    --backdrop: #e4e2e0;
    --card: #ffffff;
    --rule: #e6d6cc;
    --plum: #3d2628;
    --address-line: #9a6a5e;
    --bio-text: #f4eeee;
    --portrait-warm: #b89a52;
    --portrait-deep: #3a3a48;
  }
  * { margin: 0; padding: 0; box-sizing: border-box; }
  html, body {
    width: 1200px;
    height: 800px;
    overflow: hidden;
    background: var(--backdrop);
    font-family: "Montserrat", Arial, sans-serif;
  }
  .postcard {
    position: absolute;
    left: 150px;
    top: 100px;
    width: 900px;
    height: 600px;
    background: var(--card);
    box-shadow: 0 6px 24px rgba(0,0,0,0.18);
  }
  .guide-rule {
    position: absolute;
    left: 0;
    width: 100%;
    height: 2px;
    background: var(--rule);
  }
  .guide-rule--top { top: 78px; }
  .guide-rule--bottom { top: 520px; }

  .bio-panel {
    position: absolute;
    left: 70px;
    top: 80px;
    width: 320px;
    height: 440px;
    background: var(--plum);
    overflow: hidden;
  }
  /* panel content reads bottom-to-top */
  .bio-panel__inner {
    position: absolute;
    width: 440px;
    height: 320px;
    left: -60px;
    top: 60px;
    transform: rotate(-90deg);
  }
  .bio-panel__portrait {
    position: absolute;
    left: 0;
    top: 0;
    width: 260px;
    height: 132px;
    border-right: 3px solid var(--card);
    border-bottom: 3px solid var(--card);
    background: linear-gradient(150deg, var(--portrait-warm) 0%, #8c7a58 40%, var(--portrait-deep) 75%, #2c2e3e 100%);
  }
  .bio-panel__text {
    position: absolute;
    left: 236px;
    top: 142px;
    width: 190px;
    color: var(--bio-text);
    font-size: 14px;
    line-height: 1.3;
    font-weight: 400;
  }
  .bio-panel__text strong {
    font-weight: 800;
    font-style: italic;
    color: #ffffff;
  }

  .address-block {
    position: absolute;
    left: 430px;
    top: 300px;
    width: 330px;
  }
  .address-block__line {
    height: 2px;
    background: var(--address-line);
    margin-bottom: 50px;
  }
</style>
</head>
<body>
  <main class="postcard">
    <div class="guide-rule guide-rule--top"></div>
    <div class="guide-rule guide-rule--bottom"></div>

    <section class="bio-panel">
      <div class="bio-panel__inner">
        <div class="bio-panel__portrait" role="img" aria-label="Professional portrait of Brennic Dwale in a dark blazer"></div>
        <p class="bio-panel__text"><strong>Brennic Dwale</strong> is a Florida Realtor and licensed Interior Decorator, Kitchen &amp; Bath Designer, and Curb Appeal Specialist with 25+ years experience in the residential design/ remodeling industry.</p>
      </div>
    </section>

    <section class="address-block" aria-label="Mailing address area">
      <div class="address-block__line"></div>
      <div class="address-block__line"></div>
      <div class="address-block__line"></div>
      <div class="address-block__line"></div>
    </section>
  </main>
</body>
</html>
```